Staffing Firm - Business Cards and Stationary
Business Cards, Letterhead, Envelopes and Brochure Layout
I need double sided standard sized Business Card [3.5" x 2"]
Use whatever fonts that you think are best.
Professional
Todd Dunlap
President/CEO
2250 North Birch Avenue, Ste 730
Houston, TX 77027
Direct Line - 832-555-0143
tdunlap@kelvor.com
www.kelvor.com
We would like them to be memorable but professional.
Possibly put the various divisions?
We will need layouts for each group/division.

```html
<!DOCTYPE html>
<html lang="en">
<head>
<meta charset="utf-8">
<title>Kelvor Staffing – Stationery Set</title>
<link href="https://fonts.googleapis.com/css2?family=Cinzel:wght@400&family=Lato:wght@400;700&display=swap" rel="stylesheet">
<style>
  :root{
    --backdrop:#231e1b;
    --paper:#ffffff;
    --ink:#3a3a3a;
    --ink-soft:#6d6d6d;
    --rule:#c9c9c9;
    --card-dark-1:#2c2c2c;
    --card-dark-2:#0d0d0d;
    --on-dark:#e8e8e8;
    --on-dark-soft:#9a9a9a;
    --div-staffing:#7a7a7a;
    --div-credit:#3f7f3f;
    --div-search:#7a2a7a;
    --div-training:#a3262a;
    --div-tech:#2b5fa0;
  }
  *{box-sizing:border-box;margin:0;padding:0}
  html,body{width:1200px;height:874px;overflow:hidden}
  body{background:var(--backdrop);font-family:"Lato",sans-serif;color:var(--ink);position:relative}

  .wordmark{font-family:"Cinzel",serif;font-weight:400;letter-spacing:.04em;line-height:1.05;display:flex;align-items:center;gap:6px;white-space:nowrap}
  .wordmark .dot{width:7px;height:7px;border-radius:50%;background:currentColor;flex:none}
  .division{font-family:"Cinzel",serif;font-size:7px;letter-spacing:.06em;margin-top:2px;white-space:nowrap}

  /* business card fronts */
  .card{position:absolute;width:236px;height:126px}
  .card-front{left:77px;background:var(--paper);padding:12px 14px;box-shadow:0 2px 6px rgba(0,0,0,.5)}
  .card-front .wordmark{font-size:15px;color:var(--ink)}
  .card-front .person{position:absolute;left:14px;bottom:16px}
  .person .name{font-size:13px;color:var(--ink)}
  .person .title{font-size:8px;color:var(--ink-soft);margin-top:2px}
  .card-front .contact{position:absolute;left:132px;top:58px;font-size:5.5px;line-height:1.55;color:var(--ink-soft);border-left:1px solid var(--rule);padding-left:7px;white-space:nowrap}

  /* business card backs */
  .card-back{left:324px;width:250px;background:linear-gradient(135deg,var(--card-dark-1),var(--card-dark-2));padding:0 16px;display:flex;align-items:center;justify-content:space-between;box-shadow:0 2px 6px rgba(0,0,0,.6)}
  .card-back .wordmark{font-size:13px;color:var(--on-dark)}
  .card-back .lines{font-size:5.5px;line-height:1.6;color:var(--on-dark-soft);text-align:left;white-space:nowrap}

  /* letterhead */
  .letterhead{position:absolute;left:600px;top:72px;width:336px;height:444px;background:var(--paper);padding:16px 18px;box-shadow:0 3px 10px rgba(0,0,0,.5)}
  .letterhead .wordmark{font-size:17px}
  .letterhead .address{position:absolute;right:18px;top:16px;font-size:5.5px;line-height:1.6;color:var(--ink-soft);white-space:nowrap}
  .letterhead .footer{position:absolute;left:18px;right:18px;bottom:14px;border-top:1px solid var(--rule);padding-top:4px;display:flex;justify-content:space-between;font-family:"Cinzel",serif;font-size:4.5px;letter-spacing:.05em;color:var(--ink-soft);white-space:nowrap}

  /* envelope */
  .envelope{position:absolute;left:619px;top:547px;width:317px;height:257px}
  .envelope .face{position:absolute;inset:0 0 auto 0;height:150px;background:var(--paper);padding:12px 14px;box-shadow:0 3px 10px rgba(0,0,0,.5)}
  .envelope .wordmark{font-size:13px}
  .envelope .return{position:absolute;left:182px;top:14px;font-size:5px;line-height:1.6;color:var(--ink-soft);white-space:nowrap}
  .envelope svg{position:absolute;left:0;top:150px}
  .envelope .flap-mark{position:absolute;left:0;right:0;top:192px;display:flex;justify-content:center}
  .envelope .flap-mark .wordmark{color:var(--on-dark);font-size:13px}
</style>
</head>
<body>

<!-- card fronts -->
<section class="card card-front" style="top:84px">
  <div class="wordmark"><span class="dot"></span>Kelvor Staffing</div>
  <div class="division" style="color:var(--div-staffing)">staffing solutions</div>
  <div class="person"><div class="name">Todd Dunlap</div><div class="title">President/CEO</div></div>
  <div class="contact">2250 North Birch Avenue, Ste 730<br>Houston, TX 77027<br>Direct Line - 832-555-0143<br>tdunlap@kelvor.com<br>www.kelvor.com</div>
</section>
<section class="card card-front" style="top:228px">
  <div class="wordmark"><span class="dot"></span>Kelvor Staffing</div>
  <div class="division" style="color:var(--div-credit)">credit and risk group</div>
  <div class="person"><div class="name">Todd Dunlap</div><div class="title">President/CEO</div></div>
  <div class="contact">2250 North Birch Avenue, Ste 730<br>Houston, TX 77027<br>Direct Line - 832-555-0143<br>tdunlap@kelvor.com<br>www.kelvor.com</div>
</section>
<section class="card card-front" style="top:372px">
  <div class="wordmark"><span class="dot"></span>Kelvor Staffing</div>
  <div class="division" style="color:var(--div-search)">professional search group</div>
  <div class="person"><div class="name">Todd Dunlap</div><div class="title">President/CEO</div></div>
  <div class="contact">2250 North Birch Avenue, Ste 730<br>Houston, TX 77027<br>Direct Line - 832-555-0143<br>tdunlap@kelvor.com<br>www.kelvor.com</div>
</section>
<section class="card card-front" style="top:516px">
  <div class="wordmark"><span class="dot"></span>Kelvor Staffing</div>
  <div class="division" style="color:var(--div-training)">training services group</div>
  <div class="person"><div class="name">Todd Dunlap</div><div class="title">President/CEO</div></div>
  <div class="contact">2250 North Birch Avenue, Ste 730<br>Houston, TX 77027<br>Direct Line - 832-555-0143<br>tdunlap@kelvor.com<br>www.kelvor.com</div>
</section>
<section class="card card-front" style="top:660px">
  <div class="wordmark"><span class="dot"></span>Kelvor Staffing</div>
  <div class="division" style="color:var(--div-tech)">technology services group</div>
  <div class="person"><div class="name">Todd Dunlap</div><div class="title">President/CEO</div></div>
  <div class="contact">2250 North Birch Avenue, Ste 730<br>Houston, TX 77027<br>Direct Line - 832-555-0143<br>tdunlap@kelvor.com<br>www.kelvor.com</div>
</section>

<!-- card backs -->
<section class="card card-back" style="top:84px">
  <div><div class="wordmark"><span class="dot"></span>Kelvor Staffing</div><div class="division" style="color:var(--on-dark-soft)">staffing solutions</div></div>
  <div class="lines">credit and risk group<br>professional search group<br>training services group<br>technology services group</div>
</section>
<section class="card card-back" style="top:228px">
  <div><div class="wordmark"><span class="dot"></span>Kelvor Staffing</div><div class="division" style="color:var(--on-dark-soft)">credit and risk group</div></div>
  <div class="lines">credit and risk group<br>professional search group<br>training services group<br>technology services group</div>
</section>
<section class="card card-back" style="top:372px">
  <div><div class="wordmark"><span class="dot"></span>Kelvor Staffing</div><div class="division" style="color:var(--on-dark-soft)">professional search group</div></div>
  <div class="lines">credit and risk group<br>professional search group<br>training services group<br>technology services group</div>
</section>
<section class="card card-back" style="top:516px">
  <div><div class="wordmark"><span class="dot"></span>Kelvor Staffing</div><div class="division" style="color:var(--on-dark-soft)">training services group</div></div>
  <div class="lines">credit and risk group<br>professional search group<br>training services group<br>technology services group</div>
</section>
<section class="card card-back" style="top:660px">
  <div><div class="wordmark"><span class="dot"></span>Kelvor Staffing</div><div class="division" style="color:var(--on-dark-soft)">technology services group</div></div>
  <div class="lines">credit and risk group<br>professional search group<br>training services group<br>technology services group</div>
</section>

<!-- letterhead -->
<section class="letterhead">
  <div class="wordmark"><span class="dot"></span>Kelvor Staffing</div>
  <div class="division" style="color:var(--div-staffing)">staffing solutions</div>
  <div class="address">2250 North Birch Avenue, Ste 730<br>Houston, TX 77027<br>832-555-0143<br>www.kelvor.com</div>
  <div class="footer"><span>credit and risk group</span><span>professional search group</span><span>training services group</span><span>technology services group</span></div>
</section>

<!-- envelope -->
<section class="envelope">
  <div class="face">
    <div class="wordmark"><span class="dot"></span>Kelvor Staffing</div>
    <div class="division" style="color:var(--div-staffing)">staffing solutions</div>
    <div class="return">2250 North Birch Avenue, Ste 730<br>Houston, TX 77027</div>
  </div>
  <svg width="317" height="107" viewBox="0 0 317 107" aria-hidden="true">
    <defs><linearGradient id="flapShade" x1="0" y1="0" x2="0" y2="1"><stop offset="0" stop-color="#2e2e2e"/><stop offset="1" stop-color="#0b0b0b"/></linearGradient></defs>
    <path d="M0 0 H317 V40 L190 102 Q158 110 127 102 L0 40 Z" fill="url(#flapShade)"/>
  </svg>
  <div class="flap-mark"><div class="wordmark"><span class="dot"></span>Kelvor Staffing</div></div>
</section>

</body>
</html>
```